QUORVANTIX Process Banner

I am looking to make an ~82" x 32" stand up vertical banner that includes our companies core values, process and service delivery. I would like to be able to take these different areas and use them in other signage and print materials as well. I have attached examples of what we are looking for along with what content we already have. The content we have is very basic. Looking for some better design and creativity on how to display our core values, process and service delivery

Core Values = Do the right thing, Service Driven, Innovative, All In

Delivery Areas = Service Delivery, Centralized Services, Strategy, Automation, Technology Alignment

Our process: assessment (find a fit), proposal, onboarding, IT Roadmap, ongoing support, monitoring, maintenance

```html
<!DOCTYPE html>
<html lang="en">
<head>
<meta charset="utf-8">
<title>QUORVANTIX Process Banner</title>
<link rel="stylesheet" href="https://fonts.googleapis.com/css2?family=Montserrat:wght@800&family=Open+Sans:ital,wght@0,300;0,400;0,600;0,700;1,300&display=swap">
<style>
  :root {
    --brand: #2ea7e3;
    --slate: #6b6c6e;
    --sky: #2fa0dc;
    --royal: #3b67b8;
    --ink: #2f2f33;
    --muted: #5a5b5e;
    --band-top: #c3c4c1;
    --band-mid: #e5e7ea;
    --band-process: #d4d5d7;
    --band-foot: #e9eaec;
    --rose: #b97d87;
    --white: #ffffff;
  }
  html, body { margin: 0; padding: 0; }
  body { width: 1200px; height: 3075px; overflow: hidden; background: var(--band-mid); }
  .banner { display: block; width: 1200px; height: 3075px; }
  .section-title { font-family: 'Montserrat', sans-serif; font-weight: 800; font-size: 88px; }
  .brand { fill: var(--brand); }
  .slate { fill: var(--slate); }
  .value-num { font-family: 'Open Sans', sans-serif; font-weight: 300; font-size: 58px; fill: var(--white); }
  .value-title { font-family: 'Open Sans', sans-serif; font-weight: 700; font-size: 23px; fill: var(--white); letter-spacing: .5px; }
  .value-body { font-family: 'Open Sans', sans-serif; font-weight: 400; font-size: 12.5px; fill: #eaf4fb; }
  .hub-title { font-family: 'Open Sans', sans-serif; font-weight: 700; font-size: 31px; fill: #666; }
  .hub-sub { font-family: 'Open Sans', sans-serif; font-weight: 300; font-size: 26px; fill: #777; }
  .area-title { font-family: 'Open Sans', sans-serif; font-weight: 400; font-size: 25px; fill: var(--sky); }
  .bullets { font-family: 'Open Sans', sans-serif; font-weight: 400; font-size: 15px; fill: var(--ink); }
  .center-label { font-family: 'Open Sans', sans-serif; font-weight: 600; font-size: 24px; fill: var(--ink); }
  .arrow-label { font-family: 'Open Sans', sans-serif; font-weight: 600; font-size: 19px; fill: var(--white); }
  .badge-num { font-family: 'Open Sans', sans-serif; font-weight: 700; font-size: 13px; fill: var(--white); }
  .card-title { font-family: 'Open Sans', sans-serif; font-weight: 700; font-size: 19px; fill: #3a3a3e; letter-spacing: .5px; }
  .card-bullets { font-family: 'Open Sans', sans-serif; font-weight: 400; font-size: 14px; fill: var(--ink); }
  .contact { font-family: 'Open Sans', sans-serif; font-weight: 400; font-size: 16px; fill: var(--muted); }
  .quote { font-family: 'Open Sans', sans-serif; font-weight: 300; font-style: italic; font-size: 34px; fill: var(--sky); }
  .icon-line { fill: none; stroke: var(--white); stroke-width: 3; stroke-linecap: round; stroke-linejoin: round; }
  .icon-blue { fill: none; stroke: var(--royal); stroke-width: 3; stroke-linecap: round; stroke-linejoin: round; }
  .icon-dark { fill: none; stroke: #444; stroke-width: 2.5; stroke-linecap: round; stroke-linejoin: round; }
  .link-blue { fill: none; stroke: var(--royal); stroke-width: 3; }
  .link-grey { fill: none; stroke: #a9abae; stroke-width: 1.5; }
  .dot-grey { fill: #a9abae; }
</style>
</head>
<body>
<svg class="banner" viewBox="0 0 1200 3075" xmlns="http://www.w3.org/2000/svg">
  <defs>
    <linearGradient id="segGrad" x1="0" y1="1" x2="1" y2="0">
      <stop offset="0" stop-color="#2fb0e6"/>
      <stop offset="1" stop-color="#3b61b3"/>
    </linearGradient>
    <linearGradient id="segGradAlt" x1="0" y1="0" x2="1" y2="1">
      <stop offset="0" stop-color="#3a63b5"/>
      <stop offset="1" stop-color="#2fa9e3"/>
    </linearGradient>
    <radialGradient id="backDisc" cx=".4" cy=".4" r=".7">
      <stop offset="0" stop-color="#eef1f6"/>
      <stop offset="1" stop-color="#b9c5d6"/>
    </radialGradient>
    <radialGradient id="pearl" cx=".45" cy=".35" r=".7">
      <stop offset="0" stop-color="#ffffff"/>
      <stop offset="1" stop-color="#e4e5e8"/>
    </radialGradient>
    <linearGradient id="arrowA" x1="0" y1="0" x2="1" y2="1">
      <stop offset="0" stop-color="#4cc0ec"/><stop offset="1" stop-color="#1e8fd0"/>
    </linearGradient>
    <linearGradient id="arrowB" x1="0" y1="0" x2="1" y2="1">
      <stop offset="0" stop-color="#3aa2e0"/><stop offset="1" stop-color="#3b67b8"/>
    </linearGradient>
    <linearGradient id="arrowC" x1="0" y1="0" x2="1" y2="1">
      <stop offset="0" stop-color="#4a8ff0"/><stop offset="1" stop-color="#1e50de"/>
    </linearGradient>
    <linearGradient id="tabGrad" x1="0" y1="0" x2="1" y2="1">
      <stop offset="0" stop-color="#2ea7e3"/><stop offset="1" stop-color="#2c55d6"/>
    </linearGradient>
    <filter id="soft" x="-20%" y="-20%" width="140%" height="140%">
      <feDropShadow dx="3" dy="5" stdDeviation="6" flood-color="#000" flood-opacity=".22"/>
    </filter>
  </defs>

  <!-- Backgrounds -->
  <rect width="1200" height="3075" fill="var(--band-mid)"/>
  <polygon points="0,0 1200,0 1200,985 0,1089" fill="var(--band-top)"/>
  <polygon points="0,1968 1200,1863 1200,2800 0,2961" fill="var(--band-process)"/>
  <polygon points="0,2961 1200,2800 1200,3075 0,3075" fill="var(--band-foot)"/>

  <!-- ===== Core values ===== -->
  <g class="core-values">
    <text class="section-title" x="600" y="124" text-anchor="middle" textLength="900" lengthAdjust="spacingAndGlyphs"><tspan class="brand">QUORVANTIX</tspan><tspan class="slate"> MODEL</tspan></text>

    <circle cx="612" cy="620" r="390" fill="url(#backDisc)" filter="url(#soft)"/>
    <circle cx="600" cy="595" r="290" fill="url(#pearl)" filter="url(#soft)"/>

    <g class="value-segments" stroke="#ffffff" stroke-opacity=".55" stroke-width="1.5" filter="url(#soft)">
      <path d="M497.8 947.2 A400 400 0 0 1 187.1 625.4 L433.3 582 A150 150 0 0 0 549.8 702.7 Z" fill="url(#segGrad)"/>
      <path d="M199.7 609.6 A385 385 0 0 1 377 229.5 L501.5 428.8 A150 150 0 0 0 432.5 576.9 Z" fill="url(#segGradAlt)"/>
      <path d="M388.5 222.6 A385 385 0 0 1 785 229.5 L660.5 428.8 A150 150 0 0 0 506 426.1 Z" fill="url(#segGradAlt)"/>
      <path d="M790.7 245.1 A375 375 0 0 1 933.4 684.3 L722 607.3 A150 150 0 0 0 664.9 431.6 Z" fill="url(#segGrad)"/>
    </g>

    <circle cx="581" cy="556" r="142" fill="url(#pearl)" filter="url(#soft)"/>
    <circle cx="581" cy="556" r="129" fill="none" stroke="var(--rose)" stroke-width="2.5"/>
    <text class="hub-title" x="579" y="557" text-anchor="middle">CORE VALUES</text>
    <text class="hub-sub" x="582" y="588" text-anchor="middle">STEPS TEMPLATE</text>

    <!-- 03 Innovative -->
    <text class="value-num" x="430" y="282">03</text>
    <text class="value-title" x="529" y="247">INNOVATIVE</text>
    <text class="value-body" x="529" y="273">Lorem ipsum dolor sit amet,</text>
    <text class="value-body" x="529" y="289">consectetur adipiscing elit.</text>
    <text class="value-body" x="529" y="305">Pellentesque id semper sem,</text>
    <text class="value-body" x="529" y="321">a ultrices metus.</text>
    <g class="icon-line" transform="translate(690,225)">
      <circle cx="22" cy="14" r="11"/>
      <path d="M22 8v12M19 11h5M19 17h5"/>
      <path d="M2 30h8l8 5h12M10 30l14-4 10 6-4 4"/>
    </g>

    <!-- 02 Service driven -->
    <text class="value-num" x="224" y="560">02</text>
    <text class="value-title" x="252" y="400">SERVICE DRIVEN</text>
    <text class="value-body" x="247" y="428">Lorem ipsum dolor sit amet, consectetur</text>
    <text class="value-body" x="247" y="444">adipiscing elit. Pellentesque id semper</text>
    <text class="value-body" x="247" y="460">sem, a ultrices metus.</text>
    <g class="icon-line" transform="translate(330,282)">
      <rect x="0" y="2" width="26" height="34" rx="3"/>
      <path d="M6 11l3 3 5-5M6 20l3 3 5-5M6 29h10M30 14l8 8-12 14h-6v-6z"/>
    </g>

    <!-- 04 All in -->
    <text class="value-num" x="757" y="368">04</text>
    <text class="value-title" x="749" y="440">ALL IN</text>
    <text class="value-body" x="749" y="462">Lorem ipsum dolor sit</text>
    <text class="value-body" x="749" y="478">amet, consectetur adipi-</text>
    <text class="value-body" x="749" y="494">scing elit. Pellentesque</text>
    <text class="value-body" x="749" y="510">id semper sem, a ultrices</text>
    <text class="value-body" x="749" y="526">metus.</text>
    <g class="icon-line" transform="translate(838,552)">
      <path d="M0 40h38M4 40V24h7v16M15 40V12h8v28M27 40V20h7v20"/>
    </g>

    <!-- 01 Do the right thing -->
    <g class="icon-line" transform="translate(245,669)">
      <circle cx="0" cy="0" r="18"/>
      <path d="M0 -10V0h8"/>
    </g>
    <text class="value-title" x="265" y="719">DO THE RIGHT THING</text>
    <text class="value-body" x="290" y="746">Lorem ipsum dolor sit amet, consectetur</text>
    <text class="value-body" x="290" y="762">adipiscing elit. Pellentesque id semper</text>
    <text class="value-body" x="290" y="778">sem, a ultrices metus.</text>
    <text class="value-num" x="426" y="886">01</text>
  </g>

  <!-- ===== Delivery area ===== -->
  <g class="delivery-area">
    <text class="section-title" x="598" y="1218" text-anchor="middle" textLength="1064" lengthAdjust="spacingAndGlyphs"><tspan class="brand">QUORVANTIX</tspan><tspan class="slate"> DELIVERY AREA</tspan></text>

    <polyline class="link-blue" points="370,1411 418,1411 478,1452"/>
    <polyline class="link-blue" points="370,1625 418,1625 478,1588"/>
    <polyline class="link-blue" points="808,1399 752,1399 694,1448"/>
    <polyline class="link-blue" points="808,1625 752,1625 694,1588"/>
    <polyline class="link-grey" points="370,1460 400,1460 430,1440 470,1440"/>
    <polyline class="link-grey" points="292,1505 405,1505 425,1488 470,1488"/>
    <polyline class="link-grey" points="270,1545 360,1545 380,1530 468,1530"/>
    <polyline class="link-grey" points="214,1581 380,1581 400,1600 470,1600"/>
    <polyline class="link-grey" points="898,1487 780,1487 760,1500 705,1500"/>
    <polyline class="link-grey" points="840,1541 770,1541 750,1552 705,1552"/>
    <polyline class="link-grey" points="990,1580 930,1580 915,1590 870,1590"/>
    <circle class="dot-grey" cx="292" cy="1505" r="4"/>
    <circle class="dot-grey" cx="270" cy="1545" r="4"/>
    <circle class="dot-grey" cx="214" cy="1581" r="4"/>
    <circle class="dot-grey" cx="898" cy="1487" r="4"/>
    <circle class="dot-grey" cx="840" cy="1541" r="4"/>
    <circle class="dot-grey" cx="990" cy="1580" r="4"/>

    <circle cx="585" cy="1516" r="102" fill="url(#pearl)" filter="url(#soft)"/>
    <path d="M564.5 1632.2 A118 118 0 0 1 517.3 1419.3" fill="none" stroke="var(--royal)" stroke-width="14"/>
    <polygon points="542,1400 506,1410 522,1433" fill="var(--royal)"/>
    <path d="M625.4 1405.1 A118 118 0 0 1 652.7 1612.7" fill="none" stroke="var(--sky)" stroke-width="14"/>
    <polygon points="628,1631 664,1622 648,1599" fill="var(--sky)"/>
    <text class="center-label" x="585" y="1525" text-anchor="middle">AUTOMATION</text>

    <g class="node" transform="translate(310,1411)">
      <circle r="62" fill="#f4f5f7" filter="url(#soft)"/>
      <circle r="50" fill="url(#pearl)"/>
      <path d="M-74 -28 A80 80 0 0 0 -66 44" fill="none" stroke="var(--royal)" stroke-width="5"/>
      <circle r="14" fill="none" stroke="#7d4fe0" stroke-width="2.5"/>
      <path d="M0 0V-14M0 0L12 6" stroke="#7d4fe0" stroke-width="2.5" fill="none"/>
      <path d="M-16 -6A18 18 0 0 1 -4 -18L-4 -6Z" fill="none" stroke="#7d4fe0" stroke-width="2"/>
    </g>
    <g class="node" transform="translate(310,1633)">
      <circle r="62" fill="#f4f5f7" filter="url(#soft)"/>
      <circle r="50" fill="url(#pearl)"/>
      <path d="M-70 -36 A80 80 0 0 0 -56 58" fill="none" stroke="var(--sky)" stroke-width="5"/>
      <path d="M-14 14v-10h6v10zM-5 14v-14h6v14zM4 14v-18h6v18z" fill="none" stroke="var(--sky)" stroke-width="2"/>
      <path d="M-14 -6L0 -14 6 -10 14 -18M8 -18h6v6" fill="none" stroke="var(--sky)" stroke-width="2"/>
    </g>
    <g class="node" transform="translate(867,1399)">
      <circle r="62" fill="#f4f5f7" filter="url(#soft)"/>
      <circle r="50" fill="url(#pearl)"/>
      <path d="M74 -28 A80 80 0 0 1 60 50" fill="none" stroke="var(--royal)" stroke-width="5"/>
      <g fill="var(--royal)">
        <rect x="-18" y="-2" width="36" height="5"/>
        <circle cx="-14" cy="-10" r="4"/><circle cx="0" cy="-12" r="4"/><circle cx="14" cy="-10" r="4"/>
        <rect x="-22" y="-6" width="6" height="14"/><rect x="16" y="-6" width="6" height="14"/>
        <rect x="-14" y="3" width="3" height="10"/><rect x="11" y="3" width="3" height="10"/>
      </g>
    </g>
    <g class="node" transform="translate(867,1621)">
      <circle r="62" fill="#f4f5f7" filter="url(#soft)"/>
      <circle r="50" fill="url(#pearl)"/>
      <path d="M72 -34 A80 80 0 0 1 52 60" fill="none" stroke="var(--sky)" stroke-width="5"/>
      <g fill="none" stroke="var(--royal)" stroke-width="2">
        <path d="M-6 8a10 10 0 1 1 12 0v5h-12z"/><path d="M-4 17h8"/>
        <path d="M-16 -10l-4 -2M16 -10l4 -2M-18 0h-4M18 0h4M0 -18v-4"/>
      </g>
    </g>

    <text class="area-title" x="64" y="1332">SERVICE</text>
    <text class="area-title" x="64" y="1363">DELIVERY</text>
    <text class="bullets" x="77" y="1394">• Modern Workplace</text>
    <text class="bullets" x="77" y="1415">• Infrastructure</text>
    <text class="bullets" x="77" y="1436">• Compliance</text>
    <text class="bullets" x="77" y="1457">• Security</text>

    <text class="area-title" x="986" y="1326">TECHNOLOGY</text>
    <text class="area-title" x="986" y="1357">ALIGNMENT</text>
    <text class="bullets" x="997" y="1395">• Solving Issues</text>
    <text class="bullets" x="997" y="1416">• Monitoring</text>
    <text class="bullets" x="997" y="1437">• Backup</text>
    <text class="bullets" x="997" y="1458">• Security</text>

    <text class="area-title" x="64" y="1559">CENTRALIZED</text>
    <text class="area-title" x="64" y="1590">SERVICES</text>
    <text class="bullets" x="77" y="1630">• Standards</text>
    <text class="bullets" x="77" y="1651">• Best Practices</text>
    <text class="bullets" x="77" y="1672">• Gap Analysis</text>

    <text class="area-title" x="981" y="1573">STRATEGY</text>
    <text class="bullets" x="988" y="1613">• Roadmap</text>
    <text class="bullets" x="988" y="1634">• Planning</text>
    <text class="bullets" x="988" y="1655">• Implementation</text>
  </g>

  <!-- ===== Process ===== -->
  <g class="process">
    <text class="section-title" x="597" y="2078" text-anchor="middle" textLength="812" lengthAdjust="spacingAndGlyphs"><tspan class="brand">QUORVANTIX</tspan><tspan class="slate"> PROCESS</tspan></text>

    <circle cx="228" cy="2610" r="188" fill="none" stroke="#c6c8cb" stroke-width="3"/>
    <polygon points="180,2600 275,2600 275,2680 310,2680 228,2755 145,2680 180,2680" fill="#c3c5c8" opacity=".75"/>

    <g class="step-arrow" transform="translate(20,2152)">
      <path d="M0 160L40 118V192Z" fill="#1a6f9a"/>
      <path d="M0 160L38 40H152L160 0L218 82L122 176L128 140H42Z" fill="url(#arrowA)" filter="url(#soft)"/>
      <circle cx="27" cy="84" r="19" fill="#fff"/>
      <path d="M21 74L36 84L21 94Z" fill="#333"/>
      <text class="arrow-label" x="122" y="80" text-anchor="middle">30min Meeting</text>
      <text class="arrow-label" x="124" y="103" text-anchor="middle">- Find a Fit -</text>
    </g>
    <g class="step-arrow" transform="translate(235,2152)">
      <path d="M0 160L40 118V192Z" fill="#264f93"/>
      <path d="M0 160L38 40H152L160 0L218 82L122 176L128 140H42Z" fill="url(#arrowB)" filter="url(#soft)"/>
      <circle cx="27" cy="84" r="19" fill="#fff"/>
      <path d="M21 74L36 84L21 94Z" fill="#333"/>
      <text class="arrow-label" x="124" y="78" text-anchor="middle">Onboard +</text>
      <text class="arrow-label" x="124" y="101" text-anchor="middle">Implementation</text>
    </g>
    <g class="step-arrow" transform="translate(450,2152)">
      <path d="M0 160L40 118V192Z" fill="#1535b0"/>
      <path d="M0 160L38 40H152L160 0L218 82L122 176L128 140H42Z" fill="url(#arrowC)" filter="url(#soft)"/>
      <circle cx="27" cy="84" r="19" fill="#fff"/>
      <path d="M21 74L36 84L21 94Z" fill="#333"/>
      <text class="arrow-label" x="128" y="80" text-anchor="middle">Assessment +</text>
      <text class="arrow-label" x="128" y="103" text-anchor="middle">Proposal</text>
    </g>

    <g class="step-box" transform="translate(80,2372)">
      <polyline class="link-grey" points="-11,-24 20,0 66,0" stroke="#555"/>
      <circle cx="-11" cy="-24" r="3" fill="#555"/>
      <rect x="0" y="0" width="160" height="230" rx="8" fill="none" stroke="#7b7d80" stroke-width="1.5"/>
      <circle cx="80" cy="-2" r="15" fill="var(--sky)"/>
      <text class="badge-num" x="80" y="3" text-anchor="middle">01</text>
      <path class="icon-dark" d="M60 40h20v22M60 40v28h14"/>
      <path d="M74 46l16 14-7 1 4 9-4 2-4-9-5 5z" fill="#333"/>
      <text class="bullets" x="8" y="113">• About your Business</text>
      <text class="bullets" x="14" y="135">About QUORVANTIX</text>
      <text class="bullets" x="8" y="157">• Our Process</text>
      <text class="bullets" x="8" y="179">• Our Approach</text>
    </g>
    <g class="step-box" transform="translate(295,2372)">
      <polyline class="link-grey" points="-11,-24 20,0 66,0" stroke="#555"/>
      <circle cx="-11" cy="-24" r="3" fill="#555"/>
      <rect x="0" y="0" width="160" height="230" rx="8" fill="none" stroke="#7b7d80" stroke-width="1.5"/>
      <circle cx="80" cy="-2" r="15" fill="var(--sky)"/>
      <text class="badge-num" x="80" y="3" text-anchor="middle">02</text>
      <path class="icon-dark" d="M60 46l10-8h24v24l-10 8H60zM60 46h24v24M84 46l10-8"/>
      <rect x="68" y="52" width="12" height="12" fill="#333"/>
      <text class="bullets" x="10" y="113">• Recommendations</text>
      <text class="bullets" x="10" y="135">• Strategic Outlook</text>
      <text class="bullets" x="10" y="157">• Services Alignment</text>
      <text class="bullets" x="10" y="179">• MSA + SOW</text>
    </g>
    <g class="step-box" transform="translate(510,2372)">
      <polyline class="link-grey" points="-11,-24 20,0 66,0" stroke="#555"/>
      <circle cx="-11" cy="-24" r="3" fill="#555"/>
      <rect x="0" y="0" width="172" height="230" rx="8" fill="none" stroke="#7b7d80" stroke-width="1.5"/>
      <circle cx="92" cy="-6" r="15" fill="var(--sky)"/>
      <text class="badge-num" x="92" y="-1" text-anchor="middle">03</text>
      <circle class="icon-dark" cx="90" cy="55" r="15"/>
      <path d="M80 54l8 8 16-18" fill="none" stroke="#333" stroke-width="4" stroke-linecap="round"/>
      <text class="bullets" x="20" y="113">• Documentation</text>
      <text class="bullets" x="20" y="135">• Activation</text>
      <text class="bullets" x="20" y="157">• Support and</text>
      <text class="bullets" x="26" y="179">Continuous</text>
      <text class="bullets" x="26" y="201">Improvement</text>
    </g>

    <g class="focus-card">
      <rect x="728" y="2165" width="188" height="229" fill="#fff" filter="url(#soft)"/>
      <rect x="744" y="2180" width="156" height="199" rx="8" fill="none" stroke="#e2e3e6"/>
      <path d="M716 2212C716 2175 733 2158 772 2153C758 2180 744 2200 716 2212Z" fill="url(#tabGrad)"/>
      <text class="card-title" x="774" y="2214">ROADMAP</text>
      <text class="card-bullets" x="747" y="2247">• Modern Workplace</text>
      <text class="card-bullets" x="747" y="2268">• Infrastructure</text>
      <text class="card-bullets" x="747" y="2289">• Compliance</text>
      <text class="card-bullets" x="747" y="2310">• Security</text>
      <g class="icon-blue" transform="translate(775,2342)">
        <circle cx="0" cy="-10" r="7"/><path d="M-12 14v-6a12 10 0 0 1 24 0v6zM0 2v12"/>
      </g>
    </g>
    <g class="focus-card">
      <rect x="965" y="2165" width="188" height="229" fill="#fff" filter="url(#soft)"/>
      <rect x="981" y="2180" width="156" height="199" rx="8" fill="none" stroke="#e2e3e6"/>
      <path d="M1165 2212C1165 2175 1148 2158 1109 2153C1123 2180 1137 2200 1165 2212Z" fill="url(#tabGrad)"/>
      <text class="card-title" x="997" y="2208">SERVICE</text>
      <text class="card-title" x="997" y="2231">DELIVERY</text>
      <text class="card-bullets" x="998" y="2253">• Solving Issues</text>
      <text class="card-bullets" x="998" y="2274">• Monitoring</text>
      <text class="card-bullets" x="998" y="2295">• Backup</text>
      <text class="card-bullets" x="998" y="2316">• Security</text>
      <g class="icon-blue" transform="translate(1092,2325)">
        <path d="M0 0h26v20H12l-6 6v-6H0z"/>
        <path d="M8 10h1M13 10h1M18 10h1" stroke-width="3"/>
      </g>
    </g>
    <g class="focus-card">
      <rect x="722" y="2501" width="191" height="224" fill="#fff" filter="url(#soft)"/>
      <rect x="738" y="2516" width="159" height="194" rx="8" fill="none" stroke="#e2e3e6"/>
      <path d="M708 2689C708 2726 725 2743 764 2748C750 2721 736 2701 708 2689Z" fill="url(#tabGrad)"/>
      <g class="icon-blue" transform="translate(773,2549)">
        <circle r="14"/><circle r="7"/><path d="M0 0l14 -14"/>
      </g>
      <text class="card-title" x="762" y="2604">ALIGNMENT</text>
      <text class="card-bullets" x="764" y="2630">• Standards</text>
      <text class="card-bullets" x="764" y="2651">• Best Practices</text>
      <text class="card-bullets" x="764" y="2672">• Gap Analysis</text>
    </g>
    <g class="focus-card">
      <rect x="959" y="2501" width="190" height="224" fill="#fff" filter="url(#soft)"/>
      <rect x="975" y="2516" width="158" height="194" rx="8" fill="none" stroke="#e2e3e6"/>
      <path d="M1163 2689C1163 2726 1146 2743 1107 2748C1121 2721 1135 2701 1163 2689Z" fill="url(#tabGrad)"/>
      <g class="icon-blue" transform="translate(1102,2539)">
        <circle r="10"/><path d="M-7 7L-18 18"/>
      </g>
      <text class="card-title" x="998" y="2600">PROJECTS</text>
      <text class="card-bullets" x="993" y="2630">• Planning</text>
      <text class="card-bullets" x="993" y="2651">• Implementation</text>
      <text class="card-bullets" x="993" y="2672">• Escalation</text>
    </g>

    <g class="focus-hub" fill="none" stroke-width="36" filter="url(#soft)">
      <path d="M829.1 2436.5A106 106 0 0 1 929.5 2336.1" stroke="var(--sky)"/>
      <path d="M940.5 2336.1A106 106 0 0 1 1040.9 2436.5" stroke="var(--royal)"/>
      <path d="M1040.9 2447.5A106 106 0 0 1 940.5 2547.9" stroke="var(--sky)"/>
      <path d="M929.5 2547.9A106 106 0 0 1 829.1 2447.5" stroke="var(--royal)"/>
    </g>
    <circle cx="935" cy="2442" r="84" fill="url(#pearl)" filter="url(#soft)"/>
    <text class="center-label" x="936" y="2451" text-anchor="middle" style="font-weight:400;font-size:25px">infographic</text>
  </g>

  <!-- ===== Footer ===== -->
  <g class="footer">
    <g fill="var(--royal)">
      <path d="M111 2968a9 9 0 0 1 9 9c0 7-9 16-9 16s-9-9-9-16a9 9 0 0 1 9-9z"/>
      <circle cx="111" cy="2977" r="3.5" fill="var(--band-foot)"/>
      <path d="M104 3004c3 0 5 5 4 7-1 2-3 2-2 5 2 4 6 7 9 8 2 0 3-2 5-2 2 0 6 2 6 5-2 4-7 4-11 2-7-3-12-9-14-16-1-5 0-9 3-9z"/>
    </g>
    <g fill="none" stroke="var(--royal)" stroke-width="2">
      <circle cx="112" cy="3049" r="10"/>
      <ellipse cx="112" cy="3049" rx="4.5" ry="10"/>
      <path d="M102 3049h20M104 3043h16M104 3055h16"/>
    </g>
    <text class="contact" x="147" y="2988">48 Halvern Quay</text>
    <text class="contact" x="147" y="3020">555 014 2286</text>
    <text class="contact" x="147" y="3053">quorvantix.net</text>

    <text class="quote" x="415" y="2994">“Lorem ipsum dolor sit amet,</text>
    <text class="quote" x="415" y="3037">consectetur adipiscing”</text>

    <g class="social-slots" fill="#f7f7f8" stroke="#d9dadd" stroke-width="2">
      <circle cx="944" cy="2986" r="21"/>
      <circle cx="1021" cy="2986" r="21"/>
      <circle cx="1099" cy="2986" r="21"/>
    </g>
  </g>
</svg>
</body>
</html>
```